Kestrel Summit 2019 Enemies of the End-Times Church Flyer

We want a church conference flyer designed. We are looking for a professional, yet catchy design that uses our brand colors and logo creatively while communicating key information of the event effectively. <br/>The flyer must include all of the following:<br/>Title: Kestrel Summit 2019<br/>Topic: The Enemies of The End-Times Church <br/>Subtitles: <br/> -How the antichrist raises an army by social behavior engineering. <br/>-How the architects of modern social constructs escaped the church's radar. <br/>-The Holy Spirit's end-times agenda:<br/> The Knock-Out Punch!<br/>Speaker: Prophet Marcus Toliver <br/>Dates/time: December 27, 28 & 29 at 6pm<br/>Location: Halvorn Community Center <br/> 241 Pellham Street <br/> Portland, ME 04102<br/>Contact info: phone: 207-555-0148 <br/>email: contact@brookmeadow.example <br/> www.vutel.example<br/>*The flyer must also include a picture of the speaker and our Vutel logo <br/>Thanks, we look forward to seeing what you come up with!

Colors

Designer to choose colors to be used in the design.

Requirements
Must have
• The flyer must include all of the following:
• Title: Kestrel Summit 2019
• Topic: The Enemies of The End-Times Church
• Subtitles:
• -How the antichrist raises an army by social behavior engineering.
• -How the architects of modern social constructs escaped the church's radar.
• -The Holy Spirit's end-times agenda:
• The Knock-Out Punch!
• Speaker: Prophet Marcus Toliver
• Dates/time: December 27, 28 & 29 at 6pm
• Location: Halvorn Community Center
• 241 Pellham Street
• Portland, ME 04102
• Contact info: phone: 207-555-0148
• email: contact@brookmeadow.example
• www.vutel.example
• *The flyer must also include a picture of the speaker and our Vutel logo
Should not have
• Pictures of crosses or church buildings

```html
<!DOCTYPE html>
<html lang="en">
<head>
<meta charset="utf-8">
<title>Kestrel Summit 2019 – The Enemies of The End-Times Church</title>
<link rel="stylesheet" href="https://fonts.googleapis.com/css2?family=Anton&family=Arimo:wght@400;700&display=swap">
<style>
  :root {
    --night: #0d1c48;
    --sky: #1d4797;
    --white: #ffffff;
    --amber: #f29b00;
    --pill: #ef9c00;
    --ink: #111111;
    --navy: #163056;
    --magenta: #b1005f;
    --rule: #ffd21a;
  }
  html, body {
    margin: 0;
    padding: 0;
    overflow: hidden;
    background: #e9e9e9;
  }
  .flyer {
    position: relative;
    width: 848px;
    height: 1200px;
    overflow: hidden;
    font-family: "Arimo", Arial, sans-serif;
    color: var(--white);
    background:
      radial-gradient(ellipse 420px 260px at 640px 430px, rgba(90,150,230,.45), transparent 70%),
      radial-gradient(ellipse 500px 300px at 300px 250px, rgba(40,90,180,.35), transparent 70%),
      linear-gradient(160deg, var(--night) 0%, var(--sky) 55%, #143a86 100%);
  }
  .title {
    position: absolute;
    left: 37px;
    top: 30px;
    width: 776px;
    margin: 0;
    font-family: "Anton", Impact, sans-serif;
    font-weight: 400;
    font-size: 72px;
    line-height: 80px;
    letter-spacing: 9px;
    text-indent: 9px;
    text-align: center;
    white-space: nowrap;
  }
  .title-rule {
    position: absolute;
    left: 39px;
    top: 113px;
    width: 773px;
    height: 2px;
    background: var(--rule);
  }
  .topic {
    position: absolute;
    left: 37px;
    top: 124px;
    width: 776px;
    margin: 0;
    font-size: 42px;
    line-height: 50px;
    font-weight: 700;
    color: var(--amber);
    text-align: center;
    white-space: nowrap;
  }
  .points {
    position: absolute;
    left: 284px;
    top: 196px;
    margin: 0;
    padding: 0;
    list-style: none;
    font-size: 25px;
    font-weight: 700;
    line-height: 31.5px;
    letter-spacing: .3px;
  }
  .points li {
    position: relative;
    padding-left: 42px;
    white-space: nowrap;
  }
  .points li::before {
    content: "";
    position: absolute;
    left: 0;
    top: 6px;
    width: 19px;
    height: 19px;
    border-radius: 50%;
    background: radial-gradient(circle at 40% 35%, #ffffff, #d8dde4);
  }
  .photo {
    position: absolute;
  }
  .photo-portrait {
    left: 0;
    top: 228px;
    width: 440px;
    height: 680px;
    border-radius: 170px 170px 0 0;
    background: linear-gradient(180deg, #3b2a22 0%, #3a3b42 38%, #8a2331 55%, #34373f 75%, #2b2d33 100%);
  }
  .photo-preaching {
    left: 434px;
    top: 400px;
    width: 392px;
    height: 508px;
    border-radius: 150px 150px 0 0;
    background: linear-gradient(180deg, #2e2019 0%, #4a3226 35%, #a9bfe0 55%, #c4d3ec 80%, #9fb2cf 100%);
  }
  .speaker {
    position: absolute;
    left: 0;
    top: 768px;
    width: 422px;
    height: 104px;
    border-radius: 0 52px 52px 0;
    background: var(--pill);
    color: var(--ink);
    text-align: center;
  }
  .speaker-name {
    margin: 0;
    padding: 20px 30px 0 0;
    font-size: 31px;
    line-height: 36px;
    font-weight: 700;
    white-space: nowrap;
  }
  .speaker-role {
    margin: 0;
    padding-right: 30px;
    font-size: 23px;
    line-height: 26px;
    font-weight: 700;
  }
  .when {
    position: absolute;
    left: 456px;
    top: 770px;
    width: 370px;
    font-weight: 700;
    font-size: 40px;
    line-height: 52px;
    text-shadow: 0 1px 3px rgba(0,0,0,.35);
  }
  .when p { margin: 0; white-space: nowrap; }
  .footer-brand {
    position: absolute;
    left: 0;
    top: 908px;
    width: 292px;
    height: 292px;
    background: var(--navy);
  }
  .brand {
    position: absolute;
    left: 30px;
    top: 112px;
    display: flex;
    align-items: center;
    gap: 14px;
  }
  .brand-dot {
    width: 26px;
    height: 26px;
    border-radius: 50%;
    background: var(--amber);
  }
  .brand-name {
    font-size: 60px;
    line-height: 66px;
    font-weight: 700;
    color: var(--white);
  }
  .footer-contact {
    position: absolute;
    left: 292px;
    top: 910px;
    width: 556px;
    height: 290px;
    background: var(--magenta);
  }
  .contact {
    position: absolute;
    left: 57px;
    top: 40px;
    margin: 0;
    font-style: normal;
    font-size: 27px;
    font-weight: 700;
    line-height: 35.5px;
    letter-spacing: .3px;
  }
  .contact span { display: block; white-space: nowrap; }
  .contact .contact-email {
    font-size: 23px;
    letter-spacing: 0;
  }
</style>
</head>
<body>
  <main class="flyer">
    <div class="photo photo-portrait" role="img" aria-label="Portrait photo of Prophet Marcus Toliver in a grey blazer over a red zip sweater"></div>
    <div class="photo photo-preaching" role="img" aria-label="Photo of the speaker preaching with a headset microphone, in a light blue checked shirt"></div>

    <h1 class="title">KESTREL SUMMIT 2019</h1>
    <div class="title-rule"></div>
    <h2 class="topic">The Enemies of The End-Times Church</h2>

    <ul class="points">
      <li>How the antichrist raises an army<br>by social behavior engineering.</li>
      <li>How the architects of modern social<br>constructs escaped the church's radar.</li>
      <li>The Holy Spirit's end-times agenda:<br>The Knock-Out Punch!</li>
    </ul>

    <div class="speaker">
      <p class="speaker-name">Prophet Marcus Toliver</p>
      <p class="speaker-role">Speaker</p>
    </div>

    <div class="when">
      <p>DECEMBER - 2019</p>
      <p>27, 28 &amp; 29 &nbsp;| 6pm</p>
    </div>

    <div class="footer-brand">
      <div class="brand">
        <span class="brand-dot"></span>
        <span class="brand-name">Vutel</span>
      </div>
    </div>

    <div class="footer-contact">
      <address class="contact">
        <span>Halvorn Community Center</span>
        <span>241 Pellham Street</span>
        <span>Portland, ME 04102</span>
        <span>Phone: 207 - 555 - 0148</span>
        <span class="contact-email">email: contact@brookmeadow.example</span>
        <span>www.vutel.example</span>
      </address>
    </div>
  </main>
</body>
</html>
```